Flyer overhaul from current flyers

I need to have our current flyers updated with a fresher look. We also need to have a new utility and real estate flyer created that will go along with the design of the new flyer. We are looking for new pictures, new overall design, same color scheme but would like to have the flyers more airy and inviting.

Target Market(s)

decision makers in the healthcare/utilty/banking/real estate sectors

Font styles to use
Other font styles liked:
• Logo is in Bell MT

Colors
0054AA
0677BA
7BADD7
CADEEF
E8F1F8

Requirements
Must have
• Close to what is currently on the existing flyers

```html
<!DOCTYPE html>
<html lang="en">
<head>
<meta charset="utf-8">
<title>Riverbend Recovery Flyers</title>
<link rel="stylesheet" href="https://fonts.googleapis.com/css2?family=Roboto:wght@400;700&family=Roboto+Condensed:wght@400&family=Roboto+Slab:wght@700&display=swap">
<style>
  :root {
    --stage: #97989a;
    --band-grey: #4a5052;
    --deep-dark: #353536;
    --sky: #05aee0;
    --ocean: #14789f;
    --navy-teal: #1b5c7d;
    --accent-cyan: #12b4e8;
    --panel-blue: #4ba3c7;
    --white: #ffffff;
  }
  * { margin: 0; padding: 0; box-sizing: border-box; }
  html, body { width: 1200px; height: 750px; overflow: hidden; background: var(--stage); }
  body { position: relative; font-family: "Roboto", Arial, sans-serif; color: var(--white); }

  .flyer { position: absolute; top: 56px; width: 466px; height: 602px; overflow: hidden; }
  .flyer--services { left: 114px; }
  .flyer--philosophy { left: 636px; }

  .flyer__body {
    position: absolute; left: 0; top: 105px; width: 466px; height: 497px;
    background: linear-gradient(180deg, var(--sky) 0%, var(--ocean) 35%, var(--navy-teal) 100%);
  }
  .flyer__shapes { position: absolute; left: 0; top: 0; width: 466px; height: 602px; }

  .header-band {
    position: absolute; left: 0; top: 26px; width: 362px; height: 80px;
    background: linear-gradient(90deg, var(--band-grey) 0%, var(--band-grey) 60%, rgba(74,80,82,0.55) 100%);
    display: flex; align-items: center; padding-left: 28px; gap: 12px;
  }
  .brand__mark { width: 40px; height: 40px; border-radius: 50%; border: 4px solid var(--white); flex: none; }
  .brand__name { font-family: "Roboto", Arial, sans-serif; font-weight: 400; font-size: 19px; line-height: 20px; letter-spacing: 0.5px; color: var(--white); white-space: nowrap; }

  .headline { position: absolute; left: 16px; top: 170px; font-weight: 700; font-size: 35px; line-height: 32px; letter-spacing: -0.3px; }
  .tagline { position: absolute; left: 17px; top: 242px; font-weight: 700; font-size: 16.5px; color: var(--accent-cyan); white-space: nowrap; }

  .feature-frame { position: absolute; left: 16px; top: 269px; width: 1px; height: 206px; background: var(--accent-cyan); }
  .feature-frame::before { content: ""; position: absolute; left: 0; top: 0; width: 285px; height: 1px; background: var(--accent-cyan); }
  .feature-frame::after { content: ""; position: absolute; left: 0; bottom: 0; width: 200px; height: 1px; background: var(--accent-cyan); }

  .feature-list { position: absolute; left: 30px; top: 275px; list-style: none; font-size: 14.5px; line-height: 18px; white-space: nowrap; }
  .feature-list li { display: flex; align-items: center; height: 18px; }
  .feature-list .tick { width: 16px; height: 14px; margin-right: 2px; flex: none; }
  .feature-list .spacer { width: 16px; margin-right: 2px; flex: none; }

  .solution-band {
    position: absolute; left: 30px; top: 371px; width: 404px; height: 37px;
    background: var(--panel-blue); text-align: center; font-weight: 700; font-size: 19px; line-height: 37px;
  }

  .service-list { position: absolute; top: 422px; list-style: none; font-size: 12.5px; line-height: 14.4px; white-space: nowrap; }
  .service-list li::before { content: "•"; display: inline-block; width: 12px; font-size: 9px; }
  .service-list--left { left: 28px; }
  .service-list--right { left: 257px; }

  .contact { position: absolute; left: 7px; top: 538px; width: 160px; text-align: center; white-space: nowrap; }
  .contact__label { font-weight: 700; font-size: 13px; letter-spacing: 0.2px; }
  .contact__phone { font-weight: 700; font-size: 20.5px; line-height: 24px; margin-top: 5px; }

  .web-bar {
    position: absolute; height: 27px; background: linear-gradient(180deg, var(--sky) 0%, var(--ocean) 100%);
    font-family: "Roboto Slab", Georgia, serif; font-weight: 700; font-size: 11.5px; line-height: 27px; text-align: center; white-space: nowrap;
  }
  .flyer--services .web-bar { left: 241px; top: 563px; width: 216px; }
  .flyer--philosophy .web-bar { left: 230px; top: 554px; width: 216px; }

  .section-title { position: absolute; left: 0; width: 436px; top: 290px; text-align: center; font-weight: 700; font-size: 32px; }
  .section-rule { position: absolute; left: 87px; top: 344px; width: 292px; height: 1px; background: var(--accent-cyan); }
  .philosophy-copy {
    position: absolute; left: 42px; top: 358px; width: 381px;
    font-family: "Roboto Condensed", Arial, sans-serif; font-size: 9.6px; line-height: 15px; text-align: justify;
  }
</style>
</head>
<body>

<section class="flyer flyer--services">
  <div class="flyer__body"></div>
  <svg class="flyer__shapes" viewBox="0 0 466 602">
    <defs>
      <linearGradient id="photoToneA" x1="0" y1="0" x2="1" y2="1">
        <stop offset="0" stop-color="#cfd2e4"/>
        <stop offset="0.45" stop-color="#b7b7c4"/>
        <stop offset="1" stop-color="#eef0f4"/>
      </linearGradient>
    </defs>
    <path d="M210 0 L466 0 L466 290 C400 302 300 302 240 246 C190 196 186 100 210 0 Z" fill="var(--deep-dark)"/>
    <path role="img" aria-label="Photo of a hand with a pen over a calculator and rising bar chart" d="M268 0 L466 0 L466 284 C410 297 318 292 270 234 C226 180 228 82 268 0 Z" fill="url(#photoToneA)"/>
    <path d="M0 500 C110 494 190 540 226 602 L0 602 Z" fill="var(--deep-dark)"/>
  </svg>

  <header class="header-band">
    <span class="brand__mark"></span>
    <span class="brand__name">RIVERBEND<br>RECOVERY</span>
  </header>

  <h1 class="headline">Financial<br>Collections</h1>
  <p class="tagline">A Forward Thinking Approach</p>

  <div class="feature-frame"></div>
  <ul class="feature-list">
    <li><span class="spacer"></span>Consumer Friendly, Professional Approach</li>
    <li><svg class="tick" viewBox="0 0 16 14"><path d="M1 8 L6 13 L15 1" fill="none" stroke="#fff" stroke-width="2"/></svg>Online Consumer Debt Negotiation Tools</li>
    <li><svg class="tick" viewBox="0 0 16 14"><path d="M1 8 L6 13 L15 1" fill="none" stroke="#fff" stroke-width="2"/></svg>Live Online Agent Chat Portals</li>
    <li><svg class="tick" viewBox="0 0 16 14"><path d="M1 8 L6 13 L15 1" fill="none" stroke="#fff" stroke-width="2"/></svg>Online Consumer Dispute/Complaint Tools</li>
    <li><svg class="tick" viewBox="0 0 16 14"><path d="M1 8 L6 13 L15 1" fill="none" stroke="#fff" stroke-width="2"/></svg>FISMA Compliant Physical and Virtual Security</li>
  </ul>

  <div class="solution-band">An Impactful, All-In-One Solution</div>

  <ul class="service-list service-list--left">
    <li>Credit Report Monitoring</li>
    <li>Address/Phone Scrubbing</li>
    <li>Compliant Collection Letters</li>
    <li>Discretionary Credit Reporting</li>
    <li>Customizable Collection Workflow</li>
  </ul>
  <ul class="service-list service-list--right">
    <li>Professional Skip Tracing</li>
    <li>Deceased/Probate Services</li>
    <li>Call Recording and Monitoring</li>
    <li>Bankruptcy Claim Services</li>
    <li>Legal Collection Services</li>
  </ul>

  <div class="contact">
    <p class="contact__label">CALL US AT</p>
    <p class="contact__phone">(555) 014-2870</p>
  </div>
  <div class="web-bar">www.riverbendrecovery.com</div>
</section>

<section class="flyer flyer--philosophy">
  <div class="flyer__body"></div>
  <svg class="flyer__shapes" viewBox="0 0 466 602">
    <defs>
      <linearGradient id="photoToneB" x1="0" y1="0" x2="1" y2="1">
        <stop offset="0" stop-color="#f4ead0"/>
        <stop offset="0.5" stop-color="#d9d6cf"/>
        <stop offset="1" stop-color="#e6eef5"/>
      </linearGradient>
    </defs>
    <path d="M210 0 L466 0 L466 290 C400 302 300 302 240 246 C190 196 186 100 210 0 Z" fill="var(--deep-dark)"/>
    <path role="img" aria-label="Photo of two people reviewing charts with a calculator, glasses and notebook on a desk" d="M268 0 L466 0 L466 284 C410 297 318 292 270 234 C226 180 228 82 268 0 Z" fill="url(#photoToneB)"/>
    <path d="M0 500 C110 494 190 540 226 602 L0 602 Z" fill="var(--deep-dark)"/>
  </svg>

  <header class="header-band">
    <span class="brand__mark"></span>
    <span class="brand__name">RIVERBEND<br>RECOVERY</span>
  </header>

  <h2 class="section-title">Our Philosophy</h2>
  <div class="section-rule"></div>
  <p class="philosophy-copy">For over 30 years, Riverbend Recovery has assisted banks and financial services companies in the reconciliation of their past due accounts. Our philosophy is to provide consistent performance by investing in our clients' accounts to ensure the maximum liquidation. By building on historically proven collection techniques and employing an ever-expanding access to data and technology, our agency has continued to improve our performance to the benefit of our clients. Our capital forward, compliance centered approach has proven to deliver the most consistent results for our financial service</p>

  <div class="contact">
    <p class="contact__label">CALL US AT</p>
    <p class="contact__phone">(555) 014-2870</p>
  </div>
  <div class="web-bar">www.riverbendrecovery.com</div>
</section>

</body>
</html>
```